VELOR Capital Partners Presentation (around 10 pages) and web design

I need a document that present my company that I can send to my prospect, client and financial partners...and the web design that goes with it.
Our company is investing in gold mines in Africa and South America but provides as well mining operational solutions and consulting in finance and restructuring for the mining industry. the last vertical business of our company is a subsidiary "Tresvin Group" that provides logistics solutions for mining companies. the logo of Velor Capital partners, the logo and the presentation of Tresvin group have already been made by PIXELHARBOR and you will find them in the files uploaded

```html
<!DOCTYPE html>
<html lang="en">
<head>
<meta charset="utf-8">
<title>VELOR Capital Partners – Company Presentation</title>
<link href="https://fonts.googleapis.com/css2?family=Poppins:wght@400;500;600;700&display=swap" rel="stylesheet">
<style>
:root{
  --page:#142a45;
  --navy:#252d3a;
  --blue:#1a9be0;
  --blue-light:#d6ecfa;
  --ink:#1c1f24;
  --muted:#555c66;
  --white:#ffffff;
  --gold:#b58a2e;
  --gold-dark:#3b2e16;
}
*{margin:0;padding:0;box-sizing:border-box}
html,body{width:1169px;height:1200px;overflow:hidden}
body{background:radial-gradient(ellipse at 50% 40%,#1b3a5e 0%,var(--page) 75%);font-family:"Poppins",sans-serif;color:var(--ink);position:relative}
.slide{position:absolute;width:367px;height:206px;background:var(--white);overflow:hidden}
.c1{left:22px}.c2{left:401px}.c3{left:779px}
.r1{top:59px}.r2{top:278px}.r3{top:497px}.r4{top:715px}.r5{top:934px}
.abs{position:absolute}
.brand{position:absolute;display:flex;align-items:center;gap:4px;font-weight:600;font-size:9px;color:var(--navy);letter-spacing:.5px;white-space:nowrap}
.brand::before{content:"";width:6px;height:6px;background:var(--blue)}
.brand.light{color:var(--white)}
.brand.sm{font-size:6.5px}
.tagline{font-weight:700;font-size:10px;line-height:14px;color:var(--blue)}
.on-blue .tagline{color:var(--white)}
.lead{font-size:6px;line-height:8.5px;color:var(--white)}
.body{font-size:4.6px;line-height:6.4px;color:var(--muted)}
.kicker{font-size:5.5px;color:var(--blue);text-transform:uppercase;letter-spacing:.2px}
.title{font-weight:600;font-size:10px;color:var(--ink);text-align:center}
.sect{font-weight:700;font-size:18px;line-height:20px;color:var(--ink)}
.num{position:absolute;width:11px;height:13px;background:var(--blue);color:var(--white);font-size:7px;font-weight:600;display:flex;align-items:center;justify-content:center}
.vrule{position:absolute;width:1px;background:#9aa1aa}
.icon{position:absolute;width:34px;height:34px;border-radius:50%;border:1.5px solid var(--blue);background:radial-gradient(circle,#fbe8c2 0%,#e8f4fc 70%)}
.icon.s{width:22px;height:22px}
.label{position:absolute;font-weight:600;font-size:5.6px;line-height:6.6px;color:var(--ink);text-align:center}
.cap{position:absolute;font-size:4.3px;line-height:5.6px;color:var(--muted);text-align:center}
.photo-gold{background:linear-gradient(135deg,#3a2d15 0%,#9c7628 45%,#e0b552 60%,#4a3a1c 100%)}
.photo-site{background:linear-gradient(135deg,#6d6458 0%,#a89a82 50%,#544a3c 100%)}
.photo-office{background:linear-gradient(135deg,#e6e9ee 0%,#b9c1cc 55%,#5c6573 100%)}
.photo-mine{background:linear-gradient(135deg,#3d3a34 0%,#7b6f5a 50%,#2e2b27 100%)}
.box{position:absolute;padding:8px 10px;color:var(--white);text-align:center}
.box h3{font-size:6.5px;font-weight:600;margin-bottom:4px}
.box p{font-size:4.3px;line-height:6px}
.tab{position:absolute;height:20px;background:var(--blue);color:var(--white);font-size:6px;font-weight:600;display:flex;align-items:center;justify-content:center;text-align:center;line-height:7px}
</style>
</head>
<body>

<!-- Cover dark -->
<section class="slide c1 r1" style="background:var(--navy)">
  <div class="brand light" style="left:25px;top:36px">VELOR Capital Partners</div>
  <div class="tagline abs" style="left:25px;top:88px">Safe.<br>Responsible.<br>Innovative.</div>
  <p class="lead abs" style="left:25px;top:137px;width:112px">We mine with integrity, protect our world, and create lasting value for all.</p>
  <svg class="abs" style="left:0;top:0" width="367" height="206" role="img" aria-label="Mining truck, gold bars and mine workers in angled panels">
    <defs><linearGradient id="g1" x1="0" y1="0" x2="1" y2="1"><stop offset="0" stop-color="#c9a24a"/><stop offset=".5" stop-color="#6e5a34"/><stop offset="1" stop-color="#2b2a28"/></linearGradient></defs>
    <polygon points="175,0 367,0 367,206 130,206" fill="url(#g1)"/>
    <polygon points="175,0 228,0 160,206 130,206" fill="#1a9be0" opacity=".85"/>
    <polygon points="320,0 367,0 367,206 285,206" fill="#1a9be0" opacity=".75"/>
  </svg>
</section>

<!-- Cover blue -->
<section class="slide c2 r1 on-blue" style="background:var(--blue)">
  <div class="brand light" style="left:25px;top:36px">VELOR Capital Partners</div>
  <div class="tagline abs" style="left:25px;top:88px">Safe.<br>Responsible.<br>Innovative.</div>
  <p class="lead abs" style="left:25px;top:137px;width:112px">We mine with integrity, protect our world, and create lasting value for all.</p>
  <svg class="abs" style="left:0;top:0" width="367" height="206" role="img" aria-label="Mining truck, gold bars and mine workers in angled panels">
    <defs><linearGradient id="g2" x1="0" y1="0" x2="1" y2="1"><stop offset="0" stop-color="#c9a24a"/><stop offset=".5" stop-color="#6e5a34"/><stop offset="1" stop-color="#2b2a28"/></linearGradient></defs>
    <polygon points="175,0 367,0 367,206 130,206" fill="url(#g2)"/>
    <polygon points="175,0 228,0 160,206 130,206" fill="#252d3a" opacity=".8"/>
    <polygon points="320,0 367,0 367,206 285,206" fill="#252d3a" opacity=".7"/>
  </svg>
</section>

<!-- About Us -->
<section class="slide c3 r1">
  <div class="title abs" style="left:0;width:367px;top:20px;font-size:8px">About Us</div>
  <div class="abs photo-gold" style="left:0;top:150px;width:367px;height:56px;clip-path:polygon(0 0,100% 0,88% 100%,0 100%)" role="img" aria-label="Underground mine tunnel and gold nuggets"></div>
  <div class="box" style="left:15px;top:41px;width:168px;height:114px;background:var(--blue)">
    <h3>OUR MISSION</h3>
    <p>"Our mission is to responsibly discover, develop, and operate high-quality gold mining assets that deliver sustainable value for our shareholders, employees, communities, and the environment. We are committed to operational excellence, ethical business practices, and long-term growth through strategic investment, innovation, and the development of world-class mining projects."</p>
  </div>
  <div class="box" style="left:183px;top:41px;width:170px;height:114px;background:var(--navy)">
    <h3>OUR VALUE</h3>
    <p>We are committed to safe and responsible mining that creates enduring value. Guided by integrity, we operate with excellence, protect the environment, and invest in the communities where we work. We respect our people, foster innovation, and pursue sustainable growth to benefit our shareholders, partners, and future generations."</p>
  </div>
</section>

<!-- Core Principles -->
<section class="slide c1 r2">
  <div class="abs" style="left:0;width:367px;top:12px;text-align:center">
    <div style="font-size:7.5px;font-weight:600;color:var(--blue)">Our Core Principles</div>
    <div style="font-size:8.5px;font-weight:700">Safe. Responsible. Innovative.</div>
    <div style="font-size:4.8px;color:var(--ink)">We mine with integrity, protect our world, and create lasting value for all.</div>
  </div>
  <div class="label" style="left:42px;top:61px;width:60px">Safety First</div>
  <div class="cap" style="left:42px;top:68px;width:60px">Protecting our people and communities above all else</div>
  <div class="icon" style="left:55px;top:90px" role="img" aria-label="Worker icon"></div>
  <div class="label" style="left:106px;top:61px;width:60px">Integrity</div>
  <div class="cap" style="left:106px;top:68px;width:60px">Acting with transparency, ethics, and accountability</div>
  <div class="icon" style="left:120px;top:90px" role="img" aria-label="Integrity icon"></div>
  <div class="label" style="left:170px;top:61px;width:70px">Operational Excellence</div>
  <div class="cap" style="left:170px;top:74px;width:70px">Driving efficiency, innovation, and quality in every project</div>
  <div class="icon" style="left:186px;top:90px" role="img" aria-label="Excellence icon"></div>
  <div class="label" style="left:240px;top:61px;width:60px">Sustainability</div>
  <div class="cap" style="left:240px;top:68px;width:60px">Minimising environmental impact and managing resources</div>
  <div class="icon" style="left:253px;top:90px" role="img" aria-label="Sustainability icon"></div>
  <div class="icon" style="left:88px;top:122px" role="img" aria-label="Partnership icon"></div>
  <div class="label" style="left:74px;top:160px;width:62px">Community Partnership</div>
  <div class="cap" style="left:74px;top:174px;width:62px">Building strong, respectful and mutually beneficial relationships</div>
  <div class="icon" style="left:152px;top:122px" role="img" aria-label="People icon"></div>
  <div class="label" style="left:142px;top:160px;width:54px">Respect for People</div>
  <div class="cap" style="left:142px;top:174px;width:54px">Valuing diversity, fairness, and inclusion</div>
  <div class="icon" style="left:220px;top:122px" role="img" aria-label="Long-term value icon"></div>
  <div class="label" style="left:206px;top:160px;width:62px">Long-Term Value</div>
  <div class="cap" style="left:206px;top:167px;width:62px">Creating enduring economic and social benefits for all stakeholders</div>
  <div class="box" style="left:295px;top:55px;width:68px;height:102px;background:var(--blue);text-align:left;padding:6px;border-radius:3px">
    <h3>OUR VISION</h3>
    <p>To be a leader in Gold asset development with innovative management and organisation solutions. We aim to provide solutions from the investment to the production and the value creation of Gold Assets around the globe.</p>
  </div>
  <div class="brand sm" style="left:318px;top:192px">VELOR</div>
</section>

<!-- What we do -->
<section class="slide c2 r2">
  <div class="abs" style="left:0;width:367px;top:27px;text-align:center">
    <div class="kicker">What we do</div>
    <div style="font-size:9px;font-weight:600;line-height:12px">We develop<br>4 vertical businesses</div>
  </div>
  <div class="abs photo-gold" style="left:8px;top:72px;width:88px;height:60px" role="img" aria-label="Gold bars"></div>
  <div class="abs photo-office" style="left:97px;top:72px;width:88px;height:60px" role="img" aria-label="Advisors reviewing documents"></div>
  <div class="abs photo-mine" style="left:186px;top:72px;width:88px;height:60px" role="img" aria-label="Mine tunnel operation"></div>
  <div class="abs photo-site" style="left:275px;top:72px;width:88px;height:60px" role="img" aria-label="Mining equipment on site"></div>
  <div class="tab" style="left:8px;top:133px;width:88px">Investment</div>
  <div class="tab" style="left:97px;top:133px;width:88px">Financial Advisory</div>
  <div class="tab" style="left:186px;top:133px;width:88px">Restructuring and<br>Operation</div>
  <div class="tab" style="left:275px;top:133px;width:88px">Logistics</div>
  <div class="brand sm" style="left:155px;top:176px">VELOR</div>
</section>

<!-- Investment -->
<section class="slide c3 r2">
  <div class="num" style="left:37px;top:45px">1</div>
  <div class="sect abs" style="left:35px;top:95px">Investment</div>
  <div class="abs photo-gold" style="left:0;top:130px;width:60px;height:76px;clip-path:polygon(0 0,40% 0,100% 100%,0 100%)" role="img" aria-label="Gold ore"></div>
  <div class="vrule" style="left:160px;top:66px;height:100px"></div>
  <div class="brand sm" style="left:170px;top:46px">VELOR</div>
  <p class="body abs" style="left:170px;top:70px;width:180px;color:var(--ink)">We are a strategic investor in the gold mining sector, committed to partnering with companies where our involvement creates measurable impact.<br><br>Beyond capital, we bring <b>deep industry expertise, technical insight, and a global network</b> to enhance project value, improve operational performance, and accelerate growth.<br><br>We invest selectively, focusing on opportunities where our <b>skills, experience, and relationships can unlock the full potential of mining assets</b> — delivering sustainable returns for all stakeholders."</p>
</section>

<!-- Financial Advisory section -->
<section class="slide c1 r3">
  <div class="num" style="left:37px;top:45px">2</div>
  <div class="sect abs" style="left:37px;top:82px">Financial<br>Advisory</div>
  <div class="abs photo-gold" style="left:0;top:125px;width:60px;height:81px;clip-path:polygon(0 0,40% 0,100% 100%,0 100%)" role="img" aria-label="Gold ore"></div>
  <div class="vrule" style="left:175px;top:72px;height:92px"></div>
  <div class="brand sm" style="left:185px;top:46px">VELOR</div>
  <div class="abs" style="left:185px;top:78px;font-size:8.5px;font-weight:600;line-height:11px">Strategic Financial<br>Advisory for the<br>Gold Mining Industry</div>
  <div class="abs" style="left:185px;top:118px;font-size:5.8px;line-height:8px">Unlocking Capital.<br>Driving Growth.<br>Navigating Complexity.</div>
</section>

<!-- About Financial Advisory -->
<section class="slide c2 r3">
  <div class="num" style="left:37px;top:45px">2</div>
  <div class="sect abs" style="left:37px;top:82px;font-size:11.5px;line-height:14px">About<br>Financial<br>Advisory</div>
  <div class="abs photo-gold" style="left:0;top:125px;width:60px;height:81px;clip-path:polygon(0 0,40% 0,100% 100%,0 100%)" role="img" aria-label="Gold ore"></div>
  <div class="vrule" style="left:163px;top:66px;height:100px"></div>
  <div class="brand sm" style="left:173px;top:46px">VELOR</div>
  <p class="body abs" style="left:173px;top:70px;width:180px;color:var(--ink)">At VELOR CAPITAL PARTNERS, we specialize in financial advisory solutions tailored to the unique needs of the gold mining sector. With deep industry knowledge and strong relationships across global capital markets, we help mining companies raise capital, structure private equity deals, navigate public listings, and manage corporate restructuring.<br><br>Whether you're an early-stage explorer or a mid-tier producer, we deliver strategic, practical, and investor-aligned advice to support your growth and long-term success.</p>
</section>

<!-- Our Services -->
<section class="slide c3 r3">
  <div class="title abs" style="left:0;width:367px;top:20px">Our Services</div>
  <div class="icon" style="left:28px;top:52px" role="img" aria-label="Capital raising icon"></div>
  <div class="icon" style="left:91px;top:52px" role="img" aria-label="Private equity icon"></div>
  <div class="icon" style="left:154px;top:52px" role="img" aria-label="Mergers icon"></div>
  <div class="icon" style="left:225px;top:52px" role="img" aria-label="Public listings icon"></div>
  <div class="icon" style="left:291px;top:52px" role="img" aria-label="Board representation icon"></div>
  <div class="label" style="left:26px;top:93px;width:56px;text-align:left">Capital Raising</div>
  <div class="cap" style="left:26px;top:102px;width:56px;text-align:left">We connect mining projects with the right investors - equity, debt, or hybrid - to fund exploration, development, or expansion.</div>
  <div class="label" style="left:90px;top:93px;width:56px;text-align:left">Private Equity Advisory</div>
  <div class="cap" style="left:90px;top:109px;width:58px;text-align:left">From structuring to deal execution and closure, our team guides clients through private equity transactions with aligned strategies and trusted investor networks.</div>
  <div class="label" style="left:150px;top:93px;width:60px;text-align:left">Mergers &amp; Acquisitions Advisory</div>
  <div class="cap" style="left:150px;top:116px;width:60px;text-align:left">We provide end-to-end M&amp;A advisory services tailored to the mining industry, with a focus on identifying value, mitigating risk, and executing strategic transactions that strengthen our clients' portfolios.</div>
  <div class="label" style="left:221px;top:93px;width:58px;text-align:left">Public Listings (IPO/RTO)</div>
  <div class="cap" style="left:221px;top:109px;width:60px;text-align:left">Comprehensive listing support including exchange selection, regulatory readiness, and capital market positioning.</div>
  <div class="label" style="left:287px;top:93px;width:60px;text-align:left">Board Representation</div>
  <div class="cap" style="left:287px;top:109px;width:60px;text-align:left">Representing investors on boards of public or private mining companies.</div>
  <div class="brand sm" style="left:28px;top:192px">VELOR</div>
</section>

<!-- Why Choose Us -->
<section class="slide c1 r4">
  <div class="title abs" style="left:0;width:367px;top:19px">Why Choose Us</div>
  <div class="icon" style="left:48px;top:44px" role="img" aria-label="Sector focus icon"></div>
  <div class="icon" style="left:132px;top:44px" role="img" aria-label="Global reach icon"></div>
  <div class="icon" style="left:205px;top:44px" role="img" aria-label="Network icon"></div>
  <div class="icon" style="left:289px;top:44px" role="img" aria-label="Experience icon"></div>
  <div class="label" style="left:30px;top:84px;width:70px">Sector Focused</div>
  <div class="cap" style="left:30px;top:92px;width:70px">100% dedicated to gold mining and natural resources</div>
  <div class="label" style="left:114px;top:84px;width:70px">Global Reach</div>
  <div class="cap" style="left:114px;top:92px;width:70px">Access to capital and partners across North America, Australia, Africa, and beyond</div>
  <div class="label" style="left:187px;top:84px;width:70px">Trusted Network</div>
  <div class="cap" style="left:187px;top:92px;width:70px">Strong relationships with institutional investors, PE firms, and capital markets professionals</div>
  <div class="label" style="left:270px;top:84px;width:72px">Proven Experience</div>
  <div class="cap" style="left:270px;top:92px;width:72px">Track record of successful deals, listings, and strategic outcomes</div>
  <div class="abs photo-mine" style="left:0;top:130px;width:367px;height:42px;clip-path:polygon(0 0,100% 0,92% 100%,0 100%)" role="img" aria-label="Dark gold mining scene"></div>
  <div class="abs" style="left:0;top:130px;width:128px;height:42px;background:var(--blue);clip-path:polygon(0 0,100% 0,90% 100%,0 100%)"></div>
  <div class="abs" style="left:12px;top:139px;width:100px;font-size:6px;font-weight:600;line-height:8px;color:var(--white);text-align:center">Our team based in Toronto, Abu Dhabi and Mauritius</div>
  <p class="abs" style="left:128px;top:138px;width:205px;font-size:4.3px;line-height:5.8px;color:var(--white)">Toronto is leading the gold industry for financing and capital market activities. Abu Dhabi became during the last decade the investment place for the mining industry in the Middle East. Mauritius is positioned as a financial hub for the African mining industry.</p>
  <div class="brand sm" style="left:30px;top:191px">VELOR</div>
</section>

<!-- Restructuring and Operation section -->
<section class="slide c2 r4">
  <div class="num" style="left:37px;top:45px">3</div>
  <div class="sect abs" style="left:37px;top:84px;font-size:14px;line-height:18px">Restructuring<br>and Operation</div>
  <div class="vrule" style="left:163px;top:70px;height:96px"></div>
  <div class="brand sm" style="left:173px;top:46px">VELOR</div>
  <div class="icon" style="left:173px;top:76px;width:26px;height:26px" role="img" aria-label="Operations icon"></div>
  <div class="abs" style="left:217px;top:82px;font-size:6px;line-height:8px">Gold Mining<br>Operational Capacity</div>
  <div class="icon" style="left:173px;top:124px;width:26px;height:26px" role="img" aria-label="Turnaround icon"></div>
  <div class="abs" style="left:217px;top:131px;font-size:6px;line-height:8px">Restructuring &amp;<br>Turnaround Capabilities</div>
</section>

<!-- Gold Mining Operational Capacity -->
<section class="slide c3 r4">
  <div class="icon" style="left:28px;top:20px;width:26px;height:26px" role="img" aria-label="Operations icon"></div>
  <div class="kicker abs" style="left:130px;top:20px;font-size:4.8px">Restructuring and operation</div>
  <div class="abs" style="left:84px;top:27px;font-size:8.5px;font-weight:700">Gold Mining Operational Capacity</div>
  <p class="body abs" style="left:28px;top:60px;width:140px;color:var(--ink)">We bring deep operational expertise across the full mining lifecycle—from exploration and feasibility through to production and closure. Our team has hands-on experience managing open-pit and underground gold mining operations in diverse jurisdictions, ensuring efficiency, safety, and compliance at every stage.<br><br>We work closely with technical teams, engineers, and geologists to assess assets, optimize production, and align operations with investor and stakeholder expectations. Whether supporting a ramp-up to commercial production or improving operating margins at producing sites, we deliver value through practical, results-driven guidance.</p>
  <div class="label" style="left:185px;top:58px;width:100px;text-align:left;font-size:6px">Capabilities include</div>
  <div class="icon s" style="left:208px;top:75px" role="img" aria-label="Assessment icon"></div>
  <div class="icon s" style="left:270px;top:75px" role="img" aria-label="Production icon"></div>
  <div class="icon s" style="left:332px;top:75px" role="img" aria-label="Cost control icon"></div>
  <div class="cap" style="left:194px;top:100px;width:50px">Operational assessment and diagnostics</div>
  <div class="cap" style="left:256px;top:100px;width:50px">Production planning and optimization</div>
  <div class="cap" style="left:318px;top:100px;width:50px">Cost control and efficiency programs</div>
  <div class="icon s" style="left:208px;top:124px" role="img" aria-label="Compliance icon"></div>
  <div class="icon s" style="left:270px;top:124px" role="img" aria-label="Planning icon"></div>
  <div class="cap" style="left:194px;top:149px;width:50px">Environmental, social &amp; regulatory compliance</div>
  <div class="cap" style="left:256px;top:149px;width:50px">CapEx and OpEx planning for project scalability</div>
  <div class="brand sm" style="left:28px;top:193px">VELOR</div>
</section>

<!-- Restructuring & Turnaround -->
<section class="slide c1 r5">
  <div class="icon" style="left:28px;top:24px;width:26px;height:26px" role="img" aria-label="Turnaround icon"></div>
  <div class="kicker abs" style="left:130px;top:21px;font-size:4.8px">Restructuring and operation</div>
  <div class="abs" style="left:65px;top:28px;font-size:8.5px;font-weight:700">Restructuring &amp; Turnaround Capabilities</div>
  <p class="body abs" style="left:30px;top:62px;width:130px;color:var(--ink)">We specialize in strategic and financial restructuring for gold mining companies facing operational or financial challenges. Our approach combines industry-specific insight with capital market acumen, allowing us to design and implement turnaround strategies that stabilize businesses and position them for sustainable growth.<br><br>From distressed asset evaluations to recapitalization strategies, we provide comprehensive advisory services that align creditors, investors, and management toward common recovery goals.</p>
  <div class="label" style="left:184px;top:63px;width:100px;text-align:left;font-size:6px">Capabilities include</div>
  <div class="icon s" style="left:206px;top:79px" role="img" aria-label="Restructuring icon"></div>
  <div class="icon s" style="left:266px;top:79px" role="img" aria-label="Balance sheet icon"></div>
  <div class="icon s" style="left:322px;top:79px" role="img" aria-label="Divestiture icon"></div>
  <div class="cap" style="left:192px;top:104px;width:50px">Financial and operational restructuring</div>
  <div class="cap" style="left:252px;top:104px;width:50px">Balance sheet optimization and debt advisory</div>
  <div class="cap" style="left:308px;top:104px;width:50px">Asset divestitures and portfolio rationalization</div>
  <div class="icon s" style="left:206px;top:129px" role="img" aria-label="Crisis management icon"></div>
  <div class="icon s" style="left:266px;top:129px" role="img" aria-label="Stakeholder icon"></div>
  <div class="cap" style="left:192px;top:154px;width:50px">Crisis management and interim support</div>
  <div class="cap" style="left:252px;top:154px;width:50px">Stakeholder negotiation and strategic communications</div>
  <div class="brand sm" style="left:30px;top:194px">VELOR</div>
</section>

<!-- Logistics -->
<section class="slide c2 r5">
  <div class="num" style="left:37px;top:45px">4</div>
  <div class="sect abs" style="left:37px;top:70px">Logistics</div>
  <div class="vrule" style="left:163px;top:58px;height:72px"></div>
  <div class="brand sm" style="left:173px;top:45px">VELOR</div>
  <p class="body abs" style="left:173px;top:70px;width:180px;color:var(--ink)">Our subsidiary Tresvin Group provides contract mining solutions and dry and wet lease of equipment for mining operations.<br>With operations in Africa and South America, Tresvin can provides the best solution to your logistics challenge in Mining operations.</p>
  <div class="abs" style="left:0;top:130px;width:370px;height:47px;background:var(--blue)"></div>
  <div class="abs" style="left:10px;top:138px;font-size:7px;font-weight:600;color:var(--white)">Tresvin Group</div>
  <div class="abs" style="left:10px;top:151px;padding:1px 5px;background:var(--navy);font-size:4.8px;color:var(--white)">www.tresvin-group.com</div>
  <div class="abs photo-site" style="left:125px;top:130px;width:246px;height:47px;clip-path:polygon(6% 0,100% 0,100% 100%,0 100%)" role="img" aria-label="Mining trucks, drilling rig and heavy equipment"></div>
</section>

<!-- Thank you -->
<section class="slide c3 r5" style="background:var(--navy)">
  <svg class="abs" style="left:0;top:0" width="367" height="206" aria-hidden="true">
    <defs><linearGradient id="tb" x1="0" y1="0" x2="1" y2="1"><stop offset="0" stop-color="#1a9be0"/><stop offset="1" stop-color="#0c3a6a"/></linearGradient></defs>
    <polygon points="250,0 300,0 230,206 180,206" fill="url(#tb)" opacity=".55"/>
    <polygon points="300,0 367,0 367,206 270,206" fill="#1c2430"/>
  </svg>
  <div class="abs" style="left:34px;top:25px;font-size:13px;font-weight:600;color:var(--blue)">Thank you</div>
  <div class="brand light" style="left:34px;top:82px">VELOR</div>
  <div class="abs" style="left:34px;top:132px;font-size:5.5px;font-weight:600;color:var(--white)">CONTACT US</div>
  <div class="abs" style="left:34px;top:146px;font-size:5.2px;line-height:8px;color:#c8d0da"><span style="color:var(--blue);font-weight:600">VELOR Capital Partners</span><br>48 Harbour Lane West<br>Toronto, Ontario M5X 2A4<br>CANADA</div>
</section>

</body>
</html>
```